Bar and Grill needs specials signage

I have attached a file called "daily specials" I need it changed - so there is 1 sign/poster for each day/special
also attached other items to show some styling. I want the new posters chalkboard format, styled along the lines of the drink designs attached.
The designs should be scaleable, and editable, I will print locally

```html
<!DOCTYPE html>
<html lang="en">
<head>
<meta charset="utf-8">
<title>Daily Specials – Monday</title>
<link rel="stylesheet" href="https://fonts.googleapis.com/css2?family=Kaushan+Script&family=Permanent+Marker&family=Smokum&family=Special+Elite&display=block">
<style>
  :root {
    --page: #ffffff;
    --board: #121212;
    --chalk: #f3e9d8;
    --chalk-dim: #d9cfbf;
    --speck: rgba(243, 233, 216, 0.16);
    --speck-soft: rgba(243, 233, 216, 0.08);
    --accent: #ef7b32;
  }
  * { margin: 0; padding: 0; box-sizing: border-box; }
  html, body { width: 1200px; height: 1200px; overflow: hidden; background: var(--page); }
  .canvas { position: relative; width: 1200px; height: 1200px; }

  .poster {
    position: absolute; left: 190px; top: 30px; width: 826px; height: 1136px;
    background-color: var(--board);
    background-image:
      radial-gradient(circle at 20% 30%, var(--speck) 0 1px, transparent 1.6px),
      radial-gradient(circle at 70% 80%, var(--speck-soft) 0 1.2px, transparent 1.8px),
      radial-gradient(circle at 45% 60%, var(--speck) 0 0.8px, transparent 1.4px),
      radial-gradient(circle at 85% 15%, var(--speck-soft) 0 1px, transparent 1.6px);
    background-size: 13px 11px, 19px 23px, 29px 17px, 37px 31px;
  }
  .frame-outer, .frame-inner { position: absolute; border: 2px solid var(--chalk-dim); opacity: 0.9; }
  .frame-outer { left: 32px; top: 20px; right: 20px; bottom: 30px; }
  .frame-inner { left: 50px; top: 38px; right: 36px; bottom: 50px; border-width: 1.5px; }

  .header-art { position: absolute; left: 0; top: 0; width: 826px; height: 340px; }
  .arc-title { font-family: "Permanent Marker", cursive; font-size: 44px; fill: var(--chalk); letter-spacing: 3px; }

  .emblem {
    position: absolute; left: 274px; top: 154px; width: 292px; height: 220px;
    background: var(--accent); border-radius: 40px;
  }

  .day {
    position: absolute; left: 0; width: 826px; top: 352px; text-align: center;
    font-family: "Kaushan Script", cursive; font-size: 128px; line-height: 1;
    color: var(--chalk);
  }

  .offer {
    position: absolute; left: 0; width: 826px; top: 570px; text-align: center;
    font-family: "Smokum", cursive; color: var(--chalk);
    font-size: 78px; line-height: 76px; padding-left: 10px;
  }
  .offer .free { font-size: 90px; position: relative; display: inline-block; }
  .offer .free::after {
    content: ""; position: absolute; left: -18px; right: -6px; bottom: 2px;
    height: 3px; background: var(--chalk); border-radius: 2px;
  }

  .site {
    position: absolute; left: 0; width: 826px; top: 1014px; text-align: center;
    font-family: "Special Elite", monospace; font-size: 21px; color: var(--chalk);
    letter-spacing: 0.5px;
  }

  .treat { position: absolute; background: var(--chalk-dim); opacity: 0.8; }
  .treat-cone { left: 78px; top: 678px; width: 84px; height: 240px; border-radius: 42px 42px 12px 12px; }
  .treat-pie { left: 78px; top: 938px; width: 188px; height: 100px; border-radius: 50%; }
  .treat-muffin { left: 626px; top: 794px; width: 116px; height: 104px; border-radius: 44px 44px 10px 10px; }
  .treat-candy { left: 574px; top: 914px; width: 176px; height: 124px; border-radius: 40%; }
</style>
</head>
<body>
<div class="canvas">
  <div class="poster">
    <div class="frame-outer"></div>
    <div class="frame-inner"></div>

    <svg class="header-art" viewBox="0 0 826 340" aria-hidden="true">
      <defs>
        <path id="title-arc" d="M 228 200 Q 416 0 604 200"/>
      </defs>
      <text class="arc-title"><textPath href="#title-arc" startOffset="50%" text-anchor="middle">DAILY SPECIALS</textPath></text>
      <g stroke="var(--chalk)" stroke-linecap="round">
        <line x1="84" y1="286" x2="246" y2="286" stroke-width="3"/>
        <line x1="100" y1="294" x2="244" y2="294" stroke-width="2"/>
        <line x1="80" y1="302" x2="236" y2="302" stroke-width="3"/>
        <line x1="580" y1="286" x2="740" y2="286" stroke-width="3"/>
        <line x1="584" y1="294" x2="734" y2="294" stroke-width="2"/>
        <line x1="590" y1="302" x2="746" y2="302" stroke-width="3"/>
      </g>
    </svg>

    <div class="emblem" role="img" aria-label="Orange dinner plate with fork, knife and spoon"></div>

    <div class="day">Monday</div>

    <div class="offer">
      Kids Eat <span class="free">FREE</span><br>
      From Our<br>
      Kids Menu<br>
      With Adult<br>
      Purchase
    </div>

    <div class="site">www.hollowbrookgrill.com</div>

    <div class="treat treat-cone" role="img" aria-label="Chalk drawing of a soft-serve ice cream cone"></div>
    <div class="treat treat-pie" role="img" aria-label="Chalk drawing of a slice of pie on a plate"></div>
    <div class="treat treat-muffin" role="img" aria-label="Chalk drawing of a muffin"></div>
    <div class="treat treat-candy" role="img" aria-label="Chalk drawing of a wrapped sweet"></div>
  </div>
</div>
</body>
</html>
```